Business Card Design Project

- makeup artist business card

- original and creative

- Elegant design

- Feel free to come out with cool designs but stick to being elegant and attractive

- Design relates to makeup

- includes name, occupation, contact numbers, email, website

- regular size business card

- round corner card

- double sided

- on 1 side it should just have the website name in the center " browsandblush.example "

Industry/Entity Type

Business

Requirements
Must have
• Marla Voss
Makeup Artist
USA: +1 (415)872-6410
Singapore: +65 83027715
marlavoss@browsandblush.example
www.browsandblush.example
Should not have
• nothing cartoon looking.
Pictures of makeup being grab from the internet.. Examples: eyes or lips.

```html
<!DOCTYPE html>
<html lang="en">
<head>
<meta charset="utf-8">
<title>Marla Voss — Makeup Artist Business Card</title>
<link rel="stylesheet" href="https://fonts.googleapis.com/css2?family=Pinyon+Script&family=Tinos&family=Arimo:wght@400;700&display=swap">
<style>
  :root {
    --page: #ffffff;
    --front-dark: #0d0d0d;
    --front-mid: #2a2a2a;
    --ink-light: #ffffff;
    --ink-soft: #d9d9d9;
    --back-light: #eeeeee;
    --back-mid: #cfcfcf;
    --back-shade: #b9b9b9;
    --accent-pink: #ec1fa6;
    --contact-ink: #3a3a3a;
    --band-1: #1a5f96;
    --band-2: #2273ac;
    --band-3: #2f86bd;
    --band-4: #3a94c8;
    --band-5: #55a6d2;
    --band-6: #79b8da;
    --band-7: #9cc7df;
    --band-8: #b7d2e1;
  }
  html, body {
    margin: 0;
    padding: 0;
    width: 968px;
    height: 1200px;
    overflow: hidden;
    background: var(--page);
  }
  .canvas {
    position: relative;
    width: 968px;
    height: 1200px;
  }
  .card {
    position: absolute;
    left: 48px;
    width: 875px;
    height: 499px;
    border-radius: 34px;
    overflow: hidden;
  }

  /* Front side */
  .card-front { top: 76px; }
  .front-texture {
    position: absolute;
    inset: 0;
    background:
      radial-gradient(ellipse at 30% 35%, rgba(70,70,70,.55) 0%, rgba(0,0,0,0) 55%),
      radial-gradient(ellipse at 75% 70%, rgba(55,55,55,.45) 0%, rgba(0,0,0,0) 50%),
      linear-gradient(160deg, var(--front-mid) 0%, var(--front-dark) 100%);
  }
  .front-name {
    position: absolute;
    left: 0;
    right: 0;
    top: 222px;
    text-align: center;
    font-family: "Pinyon Script", cursive;
    font-size: 100px;
    line-height: 1;
    color: var(--ink-light);
    margin: 0;
    font-weight: 400;
  }
  .front-occupation {
    position: absolute;
    left: 0;
    right: 0;
    top: 354px;
    text-align: center;
    padding-left: 10px;
    font-family: "Tinos", serif;
    font-size: 18px;
    letter-spacing: 1px;
    color: var(--ink-soft);
    margin: 0;
  }

  /* Back side */
  .card-back {
    top: 626px;
    background: radial-gradient(ellipse at 35% 45%, var(--back-light) 0%, var(--back-mid) 70%, var(--back-shade) 100%);
  }
  .top-band {
    position: absolute;
    top: 0;
    left: 0;
    width: 875px;
    height: 26px;
  }
  .tile-grid {
    position: absolute;
    top: 26px;
    left: 0;
    width: 875px;
    height: 473px;
  }
  .back-watermark {
    position: absolute;
    left: 22px;
    top: 168px;
    white-space: nowrap;
    font-family: "Pinyon Script", cursive;
    font-size: 150px;
    line-height: 1;
    color: rgba(255,255,255,.55);
    margin: 0;
  }
  .back-website {
    position: absolute;
    left: 0;
    right: 0;
    top: 178px;
    text-align: center;
    font-family: "Arimo", sans-serif;
    font-size: 62px;
    color: var(--accent-pink);
    margin: 0;
    font-weight: 400;
  }
  .website-shadow {
    position: absolute;
    left: 150px;
    top: 262px;
    width: 575px;
    height: 18px;
    border-radius: 50%;
    background: radial-gradient(ellipse at center, rgba(0,0,0,.14) 0%, rgba(0,0,0,0) 70%);
  }
  .contact-list {
    position: absolute;
    left: 250px;
    top: 375px;
    margin: 0;
    display: grid;
    grid-template-columns: 256px auto;
    column-gap: 10px;
    row-gap: 4px;
    font-family: "Arimo", sans-serif;
    font-size: 15.5px;
    line-height: 19px;
  }
  .contact-label {
    text-align: right;
    color: var(--ink-light);
    font-weight: 700;
    margin: 0;
  }
  .contact-value {
    color: var(--contact-ink);
    margin: 0;
  }
</style>
</head>
<body>
<div class="canvas">

  <section class="card card-front">
    <div class="front-texture" role="img" aria-label="Dark charcoal grunge texture background"></div>
    <h1 class="front-name">Marla Voss</h1>
    <p class="front-occupation">MAKEUP ARTIST</p>
  </section>

  <section class="card card-back">
    <svg class="top-band" viewBox="0 0 875 26" aria-hidden="true">
      <rect x="0" y="0" width="110" height="26" fill="var(--band-1)"/>
      <rect x="110" y="0" width="100" height="26" fill="var(--band-2)"/>
      <rect x="210" y="0" width="95" height="26" fill="var(--band-3)"/>
      <rect x="305" y="0" width="120" height="26" fill="var(--band-2)"/>
      <rect x="425" y="0" width="105" height="26" fill="var(--band-4)"/>
      <rect x="530" y="0" width="90" height="26" fill="var(--band-5)"/>
      <rect x="620" y="0" width="95" height="26" fill="var(--band-6)"/>
      <rect x="715" y="0" width="85" height="26" fill="var(--band-7)"/>
      <rect x="800" y="0" width="75" height="26" fill="var(--band-8)"/>
    </svg>
    <svg class="tile-grid" viewBox="0 0 875 473" aria-hidden="true">
      <g fill="#ffffff">
        <rect x="430" y="0" width="90" height="60" opacity=".12"/>
        <rect x="560" y="0" width="80" height="70" opacity=".18"/>
        <rect x="690" y="0" width="90" height="55" opacity=".14"/>
        <rect x="780" y="40" width="95" height="80" opacity=".12"/>
        <rect x="640" y="70" width="70" height="60" opacity=".1"/>
        <rect x="800" y="300" width="75" height="90" opacity=".1"/>
        <rect x="690" y="390" width="110" height="83" opacity=".12"/>
        <rect x="560" y="420" width="90" height="53" opacity=".08"/>
      </g>
    </svg>
    <p class="back-watermark" aria-hidden="true">Marla Voss</p>
    <div class="website-shadow" aria-hidden="true"></div>
    <h2 class="back-website">browsandblush.example</h2>
    <dl class="contact-list">
      <dt class="contact-label">website ·</dt>
      <dd class="contact-value">www.browsandblush.example</dd>
      <dt class="contact-label">email ·</dt>
      <dd class="contact-value">marlavoss@browsandblush.example</dd>
      <dt class="contact-label">phone ·</dt>
      <dd class="contact-value">USA: +1 (415)872-6410</dd>
      <dt class="contact-label"></dt>
      <dd class="contact-value">Singapore: +65 83027715</dd>
    </dl>
  </section>

</div>
</body>
</html>
```